Dog Snacks brand needs a new packaging design

Dear Designers,

We are looking for a packaging expert to design our new line of Dog Snacks which contain a relaxing hemp extract (CBD).

Our company is already selling various relaxing cat & dog products , and we would like this new design to reflect the same "style & feeling" as our current products (see attached instructions).

Technical aspects:
- The packaging is a Stand Up Pouch (12x18.5x7cm - see attached instructions).
- Please follow technical guidelines from printer (see attached instructions).
- The packaging will contain 120g of high-quality, semi-moist dog snacks.
- We will be designing 3 differents variations for 3 different flavours: Chicken, Beef & Liver.
- The packaging will be printed with a matt finish.

Design aspects:
- The design should be compatible with our brand identity (i.e. fluffly, pure, relaxing, positive, clean & natural).
- Soft/rounded shapes are preferred.
- Please use our brand's colors (#3BA384, White & Black).
- Please use our company logo (see attached instructions).
- The design also needs to convey a strong sense of professionalism as we are an animal "healthcare" brand.
- If you want to include a dog picture, we would prefer you to use a picture of our official brand ambassador (see attached instructions).
- We have attached a number of packaging examples which we like a lot. (see attached instructions). Please only use those as general inspiration.
- Only original work (no plagiarism will be accepted).

Please don't hesitate to send us a message if you have any questions about the brand, the product or the design requirements.

We look forward to seeing your designs & working on this together !

Thanks & regards,
Marcus

Dog owners

Pet Care

Sans Serif

• Please see project description.

```html
<!DOCTYPE html>
<html lang="en">
<head>
<meta charset="utf-8">
<title>SnuggleBite CBD Treats – Simply Chicken</title>
<link rel="stylesheet" href="https://fonts.googleapis.com/css2?family=Montserrat:wght@500;600&family=Raleway:wght@300;400&family=Abril+Fatface&family=Playfair+Display:wght@700&display=swap">
<style>
  :root {
    --page: #ffffff;
    --teal-bg: #9ad8d6;
    --teal-light: #b4e3e0;
    --brand-green: #3ba384;
    --strip-green: #6fbfa8;
    --deep-teal: #1d6b63;
    --ink: #14231e;
    --white: #ffffff;
  }
  * { margin: 0; padding: 0; box-sizing: border-box; }
  html, body { width: 1200px; height: 827px; overflow: hidden; background: var(--page); }
  .label {
    position: absolute; left: 320px; top: 26px;
    width: 560px; height: 774px;
    background: var(--teal-bg);
    overflow: hidden;
    font-family: "Montserrat", sans-serif;
  }
  .paw-pattern {
    position: absolute; inset: 0 0 74px 0;
    background:
      radial-gradient(circle at 12% 8%, rgba(255,255,255,.28) 0, rgba(255,255,255,0) 48px),
      radial-gradient(circle at 86% 10%, rgba(255,255,255,.26) 0, rgba(255,255,255,0) 44px),
      radial-gradient(circle at 24% 31%, rgba(255,255,255,.22) 0, rgba(255,255,255,0) 40px),
      radial-gradient(circle at 92% 32%, rgba(255,255,255,.24) 0, rgba(255,255,255,0) 46px),
      radial-gradient(circle at 10% 52%, rgba(255,255,255,.22) 0, rgba(255,255,255,0) 50px),
      radial-gradient(circle at 86% 52%, rgba(255,255,255,.26) 0, rgba(255,255,255,0) 52px),
      radial-gradient(circle at 96% 78%, rgba(255,255,255,.20) 0, rgba(255,255,255,0) 40px);
  }
  .label-shapes { position: absolute; inset: 0; }
  .brand-row {
    position: absolute; top: 28px; left: 0; width: 100%;
    display: flex; align-items: center; justify-content: center; gap: 10px;
  }
  .brand-dot { width: 22px; height: 22px; border-radius: 50%; background: var(--brand-green); }
  .brand {
    font-family: "Montserrat", sans-serif; font-weight: 600;
    font-size: 25px; letter-spacing: 1px; color: var(--ink);
  }
  .brand-sub {
    position: absolute; top: 64px; left: 0; width: 100%; text-align: center;
    padding-left: 90px;
    font-family: "Raleway", sans-serif; font-size: 10px; color: var(--deep-teal);
  }
  .band-text {
    position: absolute; top: 105px;
    font-size: 11.5px; font-weight: 600; letter-spacing: .6px; color: var(--white);
  }
  .band-text.weight { left: 29px; }
  .band-text.dose { right: 28px; }
  .band-text b { font-size: 14px; }
  .benefits {
    position: absolute; top: 174px; left: 0; width: 100%; text-align: center;
    font-size: 13px; font-weight: 600; letter-spacing: 2px; color: var(--deep-teal);
  }
  .product-name {
    position: absolute; top: 188px; left: 0; width: 100%; text-align: center;
    font-family: "Raleway", sans-serif; font-weight: 300;
    font-size: 66px; letter-spacing: -2px; color: var(--deep-teal);
  }
  .product-name sup { font-size: 10px; letter-spacing: 0; vertical-align: 44px; }
  .product-type {
    position: absolute; top: 268px; left: 0; width: 100%; text-align: center;
    font-family: "Raleway", sans-serif; font-weight: 400;
    font-size: 32px; letter-spacing: -1px; color: var(--deep-teal);
  }
  .flavour-lead {
    position: absolute; top: 326px; left: 282px;
    font-family: "Playfair Display", serif; font-weight: 700;
    font-size: 32px; color: var(--white);
  }
  .flavour {
    position: absolute; top: 364px; left: 302px;
    font-family: "Abril Fatface", serif; font-size: 40px; color: var(--deep-teal);
  }
  .dog-photo {
    position: absolute; left: 0; top: 338px; width: 262px; height: 362px;
    background: radial-gradient(ellipse at 55% 40%, #fbfaf8 0%, #ece8e4 60%, #d9d3cf 100%);
    border-radius: 110px 140px 0 0;
  }
  .treat-photo { position: absolute; left: 258px; top: 462px; }
  .thc-badge {
    position: absolute; left: 446px; top: 612px; width: 78px; height: 78px;
    border-radius: 50%; background: var(--brand-green);
    outline: 3px dotted var(--brand-green); outline-offset: 4px;
    color: var(--white); text-align: center; line-height: 1;
    padding-top: 15px;
  }
  .thc-badge .big { font-size: 20px; font-weight: 600; display: block; }
  .thc-badge .mid { font-size: 14px; font-weight: 600; display: block; }
  .thc-badge .small { font-size: 8px; font-weight: 500; display: block; margin-top: 2px; }
  .claim {
    position: absolute; top: 734px; left: 0; width: 100%; text-align: center;
    font-size: 14px; font-weight: 500; color: var(--white);
  }
</style>
</head>
<body>
  <main class="label">
    <div class="paw-pattern" role="img" aria-label="Faint white paw-print pattern across the teal background"></div>

    <svg class="label-shapes" width="560" height="774" viewBox="0 0 560 774" aria-hidden="true">
      <path class="top-band" fill="#3ba384"
        d="M0,103 H560 V124 H390 Q310,124 280,157 Q250,124 170,124 H0 Z"/>
      <path class="treat-backdrop" fill="#3ba384"
        d="M300,480 Q320,432 420,430 Q468,432 474,476 L474,520 L300,520 Z"/>
      <path class="bottom-band" fill="#3ba384"
        d="M0,700 H200 Q262,700 280,668 Q298,700 360,700 H560 V724 H0 Z"/>
      <rect class="bottom-strip" x="0" y="724" width="560" height="50" fill="#6fbfa8"/>
    </svg>

    <div class="brand-row">
      <span class="brand-dot"></span>
      <span class="brand">VERDALIA</span>
    </div>
    <div class="brand-sub">For Animals</div>

    <div class="band-text weight">NET WEIGHT 120G</div>
    <div class="band-text dose">CBD <b>250</b>mg</div>

    <div class="benefits">SUPPORT · CALM · EASE</div>
    <h1 class="product-name">SnuggleBite<sup>TM</sup></h1>
    <div class="product-type">CBD Treats</div>

    <div class="flavour-lead">Simply</div>
    <div class="flavour">Chicken</div>

    <div class="dog-photo" role="img" aria-label="Photo of the white wrinkled brand ambassador dog, shown in profile"></div>

    <svg class="treat-photo" width="260" height="210" viewBox="0 0 260 210" role="img" aria-label="Photo of bone-shaped chicken dog treats">
      <defs>
        <radialGradient id="treatTone" cx="50%" cy="45%" r="60%">
          <stop offset="0%" stop-color="#d9b98f"/>
          <stop offset="100%" stop-color="#a47e57"/>
        </radialGradient>
      </defs>
      <path fill="url(#treatTone)"
        d="M12,105 Q0,38 88,18 Q176,0 232,38 Q266,66 254,134 Q242,196 154,204 Q58,212 28,172 Q15,144 12,105 Z"/>
    </svg>

    <div class="thc-badge">
      <span class="big">NO</span>
      <span class="mid">THC</span>
      <span class="small">0% THC</span>
    </div>

    <p class="claim">“Recommended By Veterinarians”</p>
  </main>
</body>
</html>
```